Flyer-Design für den Verkauf von Babyalben
Zielgruppe
Familien und Verwandte die gerade ein Baby bekommen haben - Flyer soll für den Verkauf von Babyalbum sein
Aufgabenstellung
Wenn aus Liebe Leben wird, bekommt das Glück einen Namen „
individuell gestaltetes Babyalbum mit Ergänzung privater Unterlagen und Namen

```html
<!DOCTYPE html>
<html lang="de">
<head>
<meta charset="utf-8">
<title>Babyalbum „Kostbare Momente“ – Flyer</title>
<link rel="stylesheet" href="https://fonts.googleapis.com/css2?family=Playfair+Display:ital,wght@0,500;1,600;1,700&family=Josefin+Sans:wght@300&display=swap">
<style>
  :root{
    --stage:#e9e8ef;
    --paper:#ffffff;
    --band:#c3eae7;
    --teal:#72d3c6;
    --orange:#f6ab63;
    --grey:#8c8c8c;
    --skin:#fbd9b5;
    --pink:#f7a3a3;
    --blue:#49addf;
  }
  *{box-sizing:border-box;margin:0;padding:0}
  html,body{width:1200px;height:800px;overflow:hidden;background:var(--stage)}
  .stage{position:relative;width:1200px;height:800px;display:flex;align-items:center;justify-content:center;gap:50px}
  .flyer{position:relative;width:540px;height:382px;background:var(--paper);overflow:hidden;box-shadow:0 8px 24px rgba(80,80,110,.18)}
  .band{position:absolute;background:var(--band)}
  .band--left{left:0;top:24px;width:280px;height:50px}
  .band--right{right:0;top:98px;width:230px;height:50px}
  .band--bottom{left:0;bottom:0;width:100%;height:78px}
  .tagline{position:absolute;font-family:"Josefin Sans",sans-serif;font-weight:300;font-size:17px;letter-spacing:4px;color:var(--grey);top:50%;transform:translateY(-45%);white-space:nowrap}
  .band--left .tagline{left:58px}
  .band--right .tagline{left:40px}
  .pacifier{position:absolute;width:22px;height:22px;border-radius:50%;top:14px}
  .band--left .pacifier{left:22px;background:linear-gradient(135deg,var(--blue),#f5c94e)}
  .band--right .pacifier{right:18px;background:linear-gradient(135deg,#f5c94e,#ef6f6f)}
  .baby-illustration{position:absolute;left:232px;top:28px;width:120px;height:110px;border-radius:50%;background:radial-gradient(circle at 45% 45%,var(--skin),#f3c499);border:5px solid var(--paper)}
  .confetti{position:absolute;left:0;top:0;width:100%;height:100%;background:linear-gradient(180deg,rgba(247,163,163,.05),rgba(114,211,198,.04) 60%,rgba(255,255,255,0));pointer-events:none}
  .hearts{position:absolute;top:22px;width:130px;height:34px;border-radius:17px;background:linear-gradient(90deg,var(--pink),var(--orange),var(--blue));opacity:.55}
  .hearts--start{left:22px}
  .hearts--end{right:22px;background:linear-gradient(90deg,var(--blue),var(--orange),var(--pink))}
  .web{position:absolute;left:170px;top:28px;display:flex;align-items:center;gap:8px;font-family:"Josefin Sans",sans-serif;font-weight:300;font-size:15px;letter-spacing:3px;color:#555}
  .brand{display:flex;align-items:center;gap:6px;font-family:"Playfair Display",serif;font-weight:500;font-size:15px;letter-spacing:0;color:#444}
  .brand-dot{width:10px;height:10px;border-radius:50%;background:#444}
  .title{position:absolute;left:0;width:100%;text-align:center;font-family:"Playfair Display",serif;font-weight:500;line-height:1.15}
  .title--main{top:156px;font-size:52px;color:var(--teal);padding-left:40px}
  .title--sub{top:220px;font-size:44px;color:var(--orange)}
  .copy{position:absolute;left:0;width:100%;text-align:center;font-family:"Playfair Display",serif;font-style:italic;font-weight:700}
  .copy--lead{top:156px;font-size:19px;line-height:1.3;color:var(--teal)}
  .copy--quote{top:188px;font-size:17px;line-height:1.3;color:var(--orange)}
  .copy--body{top:240px;font-size:12px;font-weight:600;line-height:1.35;color:var(--teal)}
</style>
</head>
<body>
<main class="stage">
  <section class="flyer flyer--front">
    <div class="confetti" role="img" aria-label="Verstreute bunte Punkte"></div>
    <div class="band band--left"><span class="pacifier" role="img" aria-label="Schnuller-Symbol"></span><span class="tagline">INDIVIDUELL</span></div>
    <div class="band band--right"><span class="tagline">LIEBEVOLL</span><span class="pacifier" role="img" aria-label="Schnuller-Symbol"></span></div>
    <div class="baby-illustration" role="img" aria-label="Illustration eines Babykopfes"></div>
    <div class="band band--bottom">
      <div class="hearts hearts--start" role="img" aria-label="Reihe kleiner Herzen"></div>
      <div class="web">www.<span class="brand"><span class="brand-dot"></span>Albumhaus</span>.eu</div>
      <div class="hearts hearts--end" role="img" aria-label="Reihe kleiner Herzen"></div>
    </div>
    <h1 class="title title--main">Babyalbum</h1>
    <p class="title title--sub">"Kostbare Momente"</p>
  </section>

  <section class="flyer flyer--back">
    <div class="confetti" role="img" aria-label="Verstreute bunte Punkte"></div>
    <div class="band band--left"><span class="pacifier" role="img" aria-label="Schnuller-Symbol"></span><span class="tagline">INDIVIDUELL</span></div>
    <div class="band band--right"><span class="tagline">LIEBEVOLL</span><span class="pacifier" role="img" aria-label="Schnuller-Symbol"></span></div>
    <div class="baby-illustration" role="img" aria-label="Illustration eines Babykopfes"></div>
    <div class="band band--bottom">
      <div class="hearts hearts--start" role="img" aria-label="Reihe kleiner Herzen"></div>
      <div class="web">www.<span class="brand"><span class="brand-dot"></span>Albumhaus</span>.eu</div>
      <div class="hearts hearts--end" role="img" aria-label="Reihe kleiner Herzen"></div>
    </div>
    <h2 class="copy copy--lead">Ein ganz besonderes Erinnerungsbuch:</h2>
    <p class="copy copy--quote">"Wenn aus Liebe Leben wird,<br>bekommt das Glück einen Namen."</p>
    <p class="copy copy--body">Unser liebevoll gestaltetes Babyalbum<br>gibt Ihren eigenen Erinnerungen in Form von<br>Fotos, Texten und Zeichnungen einen Rahmen.</p>
  </section>
</main>
</body>
</html>
```